Dental Office Looking for Modern, simple business cards

We just acquired our logo. Now we would like to make business cards. We are a dental office with two doctors. We are husband and wife and have a small boutique dental practice in a small town. We love our patients and they are always asking us to give our business cards to their friends. Please help us make business cards :-)

Target Market(s)

30-60 yr old

Industry/Entity Type

Dental Clinic

Contact Information for Business Card

Birch Hollow Dental P.C.
Family and Cosmetic Dentistry
4826 Delmore Rd. Marlow Falls VT 12417
Tel: 518 642 7731 Fax: 518 642 7048

Dr. Tomas K. Brellin DDS
Dr. Marisol Ede Thornquist DDS

Font styles to use
Serif
Sans Serif

Requirements
Must have
• Simple clean design, modern, colorful. Should incorporate the logo.
Nice to have
• dental imagery ( teeth, smile, etc ...).

```html
<!DOCTYPE html>
<html lang="en">
<head>
<meta charset="utf-8">
<title>Birch Hollow Dental – Business Card</title>
<link href="https://fonts.googleapis.com/css2?family=Lato:wght@400;700&display=swap" rel="stylesheet">
<style>
  :root {
    --bg: #3a3a3c;
    --card-white: #f7f7f7;
    --card-blue: #0b6fb4;
    --card-blue-deep: #0a62a0;
    --brand-blue: #1a72c0;
    --text-grey: #4a4a4a;
    --rule-grey: #b9b9b9;
  }
  * { box-sizing: border-box; margin: 0; padding: 0; }
  html, body {
    width: 1200px; height: 1021px; overflow: hidden;
    background: var(--bg);
    font-family: "Lato", Arial, sans-serif;
  }
  .stage {
    width: 1200px; height: 1021px;
    display: flex; flex-direction: column; align-items: center; justify-content: center;
    gap: 52px;
  }
  .card {
    width: 760px; height: 434px;
    border-radius: 26px;
    position: relative;
    overflow: hidden;
  }
  .card--back {
    background: var(--card-blue);
    display: flex; align-items: center; justify-content: center;
  }
  .back-mark {
    display: flex; align-items: center; gap: 14px;
    color: var(--card-blue-deep);
    font-weight: 700; font-size: 30px; letter-spacing: 0.5px;
  }
  .back-mark__dot {
    width: 22px; height: 22px; border-radius: 50%;
    background: var(--card-blue-deep);
  }
  .card--front {
    background: var(--card-white);
    display: flex; align-items: center;
  }
  .brand {
    width: 52%;
    display: flex; align-items: center; justify-content: center; gap: 12px;
    color: var(--brand-blue);
    font-weight: 700; font-size: 34px;
  }
  .brand__dot {
    width: 20px; height: 20px; border-radius: 50%;
    background: var(--brand-blue);
  }
  .divider {
    width: 2px; height: 250px;
    background: var(--rule-grey);
  }
  .details {
    padding-left: 36px;
    color: var(--text-grey);
    font-size: 19px; line-height: 1.3;
  }
  .doctors {
    color: var(--brand-blue);
    font-weight: 700; font-size: 21px; line-height: 1.25;
    margin-bottom: 18px;
  }
  .practice { color: var(--brand-blue); }
  .contact { margin-top: 12px; }
  .contact__line { display: flex; align-items: center; gap: 8px; }
  .contact__line svg { width: 16px; height: 16px; fill: var(--brand-blue); flex: none; }
</style>
</head>
<body>
<main class="stage">
  <section class="card card--back">
    <div class="back-mark"><span class="back-mark__dot"></span>Birch Hollow Dental</div>
  </section>

  <section class="card card--front">
    <div class="brand"><span class="brand__dot"></span>Birch Hollow Dental</div>
    <div class="divider"></div>
    <div class="details">
      <p class="doctors">Dr. Tomas K. Brellin DDS<br>Dr. Marisol Ede Thornquist DDS</p>
      <p class="practice">Birch Hollow Dental P.C.</p>
      <p>Family and Cosmetic Dentistry</p>
      <p>4826 Delmore Rd.</p>
      <p>Marlow Falls VT 12417</p>
      <div class="contact">
        <p class="contact__line">
          <svg viewBox="0 0 24 24" aria-hidden="true"><path d="M6.6 10.8a15.1 15.1 0 0 0 6.6 6.6l2.2-2.2a1 1 0 0 1 1-.25 11.4 11.4 0 0 0 3.6.57 1 1 0 0 1 1 1V20a1 1 0 0 1-1 1A17 17 0 0 1 3 4a1 1 0 0 1 1-1h3.5a1 1 0 0 1 1 1c0 1.25.2 2.45.57 3.57a1 1 0 0 1-.25 1z"/></svg>
          802 642 7731
        </p>
        <p class="contact__line">
          <svg viewBox="0 0 24 24" aria-hidden="true"><path d="M7 3h10v5H7zM4 9h16a2 2 0 0 1 2 2v6h-4v4H6v-4H2v-6a2 2 0 0 1 2-2zm4 7v3h8v-3z"/></svg>
          802 642 7048
        </p>
      </div>
    </div>
  </section>
</main>
</body>
</html>
```